Study Lantern

StudyLantern.com will be a place for people looking for information, resources, and advisement to start or continue their education. We want a friendly, inviting site design that makes finding what potential students are looking for simple and easy to navigate. We are not committed to the colors of the logo, so variations on the color scheme are welcome.

Text instructions based on the wireframe: For the site's homepage we'd like a banner at the very top for our Logo and white space to the right of it. See attachments for logo + wireframe. Below that would be navigation. Below that split into 2/3 on the left we would have home page content, and 1/3 on the right we would have the lead form. At the bottom of the page we would have a space for types of degrees, then a footer with copyright info + site info.

See wireframes for additional page layouts.

Industry/Entity Type

Education

Requirements
Must have
• At minimum we are looking for three pages: homepage, choose your degree path page, and content page.
Nice to have
• -White space is appreciated
-Variations on the color scheme are welcome, we are not married to the existing logo's color scheme.

```html
<!DOCTYPE html>
<html lang="en">
<head>
<meta charset="utf-8">
<title>Study Lantern – Home</title>
<link href="https://fonts.googleapis.com/css2?family=Ubuntu:ital,wght@0,400;0,500;1,400;1,500&display=swap" rel="stylesheet">
<style>
:root{
  --charcoal:#3b3b3b;
  --charcoal-dark:#2f2f2f;
  --orange:#f05a0e;
  --orange-light:#ff7a2a;
  --red-head:#e3260f;
  --cream:#fdf1cc;
  --ink:#333;
  --panel-edge:#dcdcdc;
  --field-line:#c9c9c9;
  --muted:#9a9a9a;
}
*{box-sizing:border-box;margin:0;padding:0}
html,body{width:926px;height:1200px;overflow:hidden}
body{position:relative;background:var(--charcoal);font-family:Tahoma,"Ubuntu",sans-serif;color:var(--ink)}
.site-header{position:absolute;left:0;top:0;width:926px;height:118px;background:var(--charcoal)}
.brand{position:absolute;left:100px;top:62px;font-family:"Ubuntu",sans-serif;font-weight:500;font-size:33px;color:#fff;letter-spacing:-.5px}
.contact{position:absolute;right:96px;top:16px;text-align:right;font-family:"Ubuntu",sans-serif;color:#fff}
.contact .label{color:var(--orange);font-size:10px;margin-right:4px}
.contact .phone{font-size:14px}
.contact .mail{font-size:14px;font-style:italic;text-decoration:underline}
.contact div+div{margin-top:3px}
.main-nav{position:absolute;left:400px;top:69px;width:430px;height:35px;border-radius:9px;background:linear-gradient(var(--orange-light),var(--orange));display:flex;overflow:hidden}
.main-nav a{flex:1;color:#fff;text-decoration:none;font-family:"Ubuntu",sans-serif;font-size:10px;display:flex;align-items:center;justify-content:center;border-left:1px solid #ffa56f}
.main-nav a:first-child{border-left:none}
.hero{position:absolute;left:0;top:118px;width:926px;height:800px;background:linear-gradient(var(--cream),#fff 38%)}
.hero svg{position:absolute;left:0;top:0}
.card{position:absolute;background:#fff;border:6px solid var(--panel-edge);border-radius:10px}
.card h2{font-family:"Ubuntu",sans-serif;font-style:italic;font-weight:500;color:var(--red-head);font-size:17px;padding-bottom:6px;border-bottom:1px solid #ddd;margin-bottom:12px}
.welcome{left:93px;top:481px;width:418px;height:464px;padding:13px 17px}
.welcome p{font-size:8.6px;line-height:11.1px;text-align:justify;margin-bottom:11px}
.lead-form{left:524px;top:481px;width:311px;height:464px;padding:13px 17px}
.lead-form .intro{font-style:italic;font-size:8.6px;line-height:11px;margin-bottom:11px}
.field-label{display:block;color:var(--orange);font-size:7.8px;margin:6px 0 3px 2px}
.field{height:16px;border:1px solid var(--field-line);font-size:7.8px;color:var(--muted);padding:3px 7px;font-style:italic;position:relative}
.field.select::after{content:"";position:absolute;right:0;top:0;width:15px;height:14px;background:var(--orange)}
.field.select svg{position:absolute;right:4px;top:4px;z-index:1}
.row{display:flex;gap:4px}
.row .field:nth-child(1){width:59px}.row .field:nth-child(2){width:131px}.row .field:nth-child(3){width:69px}
.submit{display:inline-block;margin-top:9px;background:var(--orange);color:#fff;font-family:"Ubuntu",sans-serif;font-size:10px;padding:6px 8px}
.required{color:var(--orange);font-size:8px;margin-top:9px}
.degrees{left:93px;top:960px;width:741px;height:186px;padding:15px 17px;display:flex}
.degree{width:335px}
.degree+.degree{margin-left:35px;position:relative}
.degree+.degree::before{content:"";position:absolute;left:-18px;top:0;width:1px;height:160px;background:#e3e3e3}
.degree h2{margin-bottom:13px}
.degree-body{display:flex;gap:8px}
.degree-photo{width:129px;height:81px;flex:none}
.degree-text{font-size:8.6px;line-height:11px;text-align:justify}
.degree-text p{margin-bottom:10px}
.degree-text a{color:var(--orange);font-style:italic;font-family:"Ubuntu",sans-serif}
.site-footer{position:absolute;left:0;top:1161px;width:926px;text-align:center;color:#fff;font-size:7.8px;line-height:12px}
.site-footer span{margin:0 5px}
</style>
</head>
<body>
<header class="site-header">
  <div class="brand">Study Lantern</div>
  <div class="contact">
    <div><span class="label">Call:</span><span class="phone">111-111-111</span></div>
    <div><span class="label">Email:</span><span class="mail">Info@studylantern.com</span></div>
  </div>
  <nav class="main-nav">
    <a href="#">About Us</a><a href="#">Contact Us</a><a href="#">Privacy Policy</a><a href="#">Terms of Use</a><a href="#">Feed Back</a>
  </nav>
</header>

<section class="hero">
  <svg width="926" height="340" viewBox="0 118 926 340">
    <defs>
      <linearGradient id="sky" x1="0" y1="0" x2="0" y2="1"><stop offset="0" stop-color="#8fb7e6"/><stop offset="1" stop-color="#1d1d22"/></linearGradient>
      <linearGradient id="dark" x1="0" y1="0" x2="0" y2="1"><stop offset="0" stop-color="#4a4a4a"/><stop offset="1" stop-color="#111"/></linearGradient>
      <linearGradient id="hands" x1="0" y1="0" x2="1" y2="1"><stop offset="0" stop-color="#2c3546"/><stop offset=".5" stop-color="#c98f74"/><stop offset="1" stop-color="#1a1a1a"/></linearGradient>
      <linearGradient id="blue" x1="0" y1="0" x2="0" y2="1"><stop offset="0" stop-color="#2a5ca4"/><stop offset="1" stop-color="#0f2b58"/></linearGradient>
    </defs>
    <g role="img" aria-label="Graduates tossing caps under a blue sky"><polygon points="93,206 240,182 240,442 93,420" fill="url(#sky)"/></g>
    <g role="img" aria-label="Two smiling graduates holding diplomas"><polygon points="240,128 387,140 387,388 240,388" fill="url(#dark)"/></g>
    <g role="img" aria-label="Handshake while a diploma is presented"><polygon points="387,158 534,158 534,418 387,418" fill="url(#hands)"/></g>
    <g role="img" aria-label="Graduate adjusting her cap"><polygon points="534,182 682,182 682,442 534,442" fill="url(#dark)"/></g>
    <g role="img" aria-label="Hand raising a rolled diploma with red ribbon"><polygon points="682,128 830,150 830,366 682,388" fill="url(#blue)"/></g>
  </svg>
</section>

<main>
  <article class="card welcome">
    <h2>Welcome to Study Lantern</h2>
    <p>The Brighter Paths Programme is a long term plan for improving the living conditions and prospects for people in the most disadvantaged communities in the region. The programme ensures that the money and support available from the Regional Assembly Government and various other publicly funded agencies are targeted at the poorest areas Our role is to coordinate community led regeneration of the area with local residents, through Valley Ridge Partnership Board, seeking cooperation from other organisations within the public, private and voluntary sector to work together with us to tackle many issues that affect the lives of people who live in the area.</p>
    <p>Local transport, access to relevant health care, activities for children and young people, services for the elderly, family support, the environment, education and training opportunities are just some of the issues that have been brought to the attention of Brighter Paths of which we are all working on at present.</p>
    <p>he Brighter Paths Programme is a long term plan for improving the living conditions and prospects for people in the most disadvantaged communities in the region. The programme ensures that the money and support available from the Regional Assembly Government and various other publicly funded agencies are targeted at the poorest areas Our role is to coordinate community led regeneration of the area with local residents, through Valley.</p>
    <p>Ridge Partnership Board, seeking cooperation from other organisations within the public, private and voluntary sector to work together with us to tackle many issues that affect the lives of people who live in the area. Local transport, access to relevant health care, activities for children and young people, services for the elderly, family support, the environment, education and training opportunities are just some of the issues that have been brought to the attention of Brighter Paths of which we are all working on at present.</p>
    <p>he Brighter Paths Programme is a long term plan for improving the living conditions and prospects for people in the most disadvantaged communities in the region. The programme ensures that the money and support available from the Regional Assembly Government and various other publicly funded agencies are targeted at the poorest areas.</p>
  </article>

  <aside class="card lead-form">
    <h2>Tell us more about YOU!</h2>
    <p class="intro">StudyLantern provides you with accredited school information that match your interests.</p>
    <p class="intro">Get matched to the right schools today.</p>
    <label class="field-label">Subject*</label>
    <div class="field select">Choose One<svg width="7" height="5" viewBox="0 0 7 5"><polygon points="0,0 7,0 3.5,5" fill="#fff"/></svg></div>
    <label class="field-label">Degree Level*</label>
    <div class="field select">Choose One<svg width="7" height="5" viewBox="0 0 7 5"><polygon points="0,0 7,0 3.5,5" fill="#fff"/></svg></div>
    <label class="field-label">High School Grad Yr.*</label>
    <div class="field select">Choose One<svg width="7" height="5" viewBox="0 0 7 5"><polygon points="0,0 7,0 3.5,5" fill="#fff"/></svg></div>
    <label class="field-label">First Name*</label>
    <div class="field">Enter First Name</div>
    <label class="field-label">Last Name*</label>
    <div class="field">Enter Last Name</div>
    <label class="field-label">Street Address*</label>
    <div class="field">Enter Street Address</div>
    <label class="field-label">Zip / City / State*</label>
    <div class="row"><div class="field"></div><div class="field"></div><div class="field"></div></div>
    <label class="field-label">Phone Number*</label>
    <div class="field">(&nbsp;&nbsp;&nbsp;)</div>
    <label class="field-label">Email Address*</label>
    <div class="field">Email Address</div>
    <div class="submit">Request Information</div>
    <p class="required">*Required fields</p>
  </aside>

  <section class="card degrees">
    <div class="degree">
      <h2>Degree Type 1</h2>
      <div class="degree-body">
        <div class="degree-photo" role="img" aria-label="Group of cheerful graduates in caps" style="background:linear-gradient(135deg,#5a4a40,#1c1c1c)"></div>
        <div class="degree-text">
          <p>Are you overwhelmed by the thought of choosing the right college?</p>
          <p>StudyLantern helps simplify this process by matching colleges to you and your needs.Tell us about yourself and let us do the work for you.Are you overwhelmed by the thought.</p>
          <a href="#">Read More</a>
        </div>
      </div>
    </div>
    <div class="degree">
      <h2>Degree Type 2</h2>
      <div class="degree-body">
        <div class="degree-photo" role="img" aria-label="Row of graduates standing in gowns" style="background:linear-gradient(135deg,#8aa3c2,#1a1a1a)"></div>
        <div class="degree-text">
          <p>Are you overwhelmed by the thought of choosing the right college?</p>
          <p>StudyLantern helps simplify this process by matching colleges to you and your needs.Tell us about yourself and let us do the work for you.Are you overwhelmed by the thought.</p>
          <a href="#">Read More</a>
        </div>
      </div>
    </div>
  </section>
</main>

<footer class="site-footer">
  <div>About us<span>|</span>Contact Us<span>|</span>Privacy Policy<span>|</span>Terms of Use<span>|</span>Feed back</div>
  <div>Copyright © 2012. Study Lantern. All Rights Reserved</div>
</footer>
</body>
</html>
```